website refresh/redesign needed for Printing e commerce website

We'd like a website refresh/redesign done with the specific goal of having the site act as a more effective funnel for leads.<br/><br/>We think that the current design is outdated.<br/><br/>We want our customers and partners to still recognize the website, Is a big chunk of our business is repeat orders. <br/>so it should not be a full redesign. General color scheme and such should remain the same so that it is clear we are the same company. <br/><br/>However, the updated website design should look more polished and convey high-quality products and services that we provide. <br/><br/>Our website is https://shopledgerformsnet.quillpaperdepot.com/ if you want to take a look at our current website design. <br/><br/>we need 3 pages redesigned... <br/><br/>1. homepage:https://shopledgerformsnet.quillpaperdepot.com/<br/><br/>2. Category page: <br/>https://shopledgerformsnet.quillpaperdepot.com/order-computer-checks-c-4.html<br/><br/>3. Product detail page: https://shopledgerformsnet.quillpaperdepot.com/voucher-computer-checks-p-35.html<br/><br/> I can provide many more pictures of our products if needed.<br/><br/><br/>BTW. I have another project here on brief bazaar, you can check the other ones too, so to make it easier to do both when working on this.<br/><br/> Please reach out to me should you have any questions or comments.

```html
<!DOCTYPE html>
<html lang="en">
<head>
<meta charset="utf-8">
<title>ShopLedgerForms.net – Business &amp; Computer Checks</title>
<link href="https://fonts.googleapis.com/css2?family=Open+Sans:wght@400;600;700&family=Roboto:wght@500;700&display=swap" rel="stylesheet">
<style>
:root{
  --green:#3a9a22;
  --green-dark:#23691a;
  --green-deep:#1d4f16;
  --ink:#2b2b2b;
  --muted:#6b6b6b;
  --line:#e3e3e3;
  --panel:#f1f1f1;
  --white:#ffffff;
}
*{box-sizing:border-box;margin:0;padding:0}
html,body{width:1200px;height:3804px;overflow:hidden}
body{font-family:"Open Sans",Arial,sans-serif;color:var(--ink);background:var(--white);font-size:13px;line-height:1.55}
.wrap{width:920px;margin:0 auto;position:relative}
h2.section-title{font-family:"Roboto",Arial,sans-serif;font-weight:700;font-size:30px;color:var(--green-dark);text-align:center}
.btn{display:inline-block;background:var(--green-dark);color:var(--white);font-weight:700;font-size:12px;letter-spacing:.5px;padding:9px 18px;text-transform:uppercase;white-space:nowrap}

/* header */
.site-header{height:132px;border-bottom:1px solid var(--line)}
.site-header .wrap{height:132px}
.brand{position:absolute;left:0;top:16px;display:flex;align-items:center;gap:10px;font-weight:700;font-size:22px;color:var(--green-dark)}
.brand-mark{width:28px;height:28px;background:var(--green)}
.main-nav{position:absolute;left:0;top:78px;display:flex;gap:26px;font-size:12px;color:var(--ink);white-space:nowrap}
.main-nav a{color:inherit;text-decoration:none;padding-bottom:8px}
.main-nav a.active{color:var(--green-dark);font-weight:700;border-bottom:3px solid var(--green)}
.account{position:absolute;right:0;top:78px;display:flex;gap:20px;align-items:center;font-size:11px;font-weight:600;white-space:nowrap}
.account span{display:flex;align-items:center;gap:6px}

/* hero */
.hero{height:328px;background:linear-gradient(100deg,var(--green-deep) 0%,var(--green-dark) 45%,var(--green) 100%);position:relative;overflow:hidden}
.hero .wrap{height:328px}
.hero h1{position:absolute;left:0;top:74px;width:440px;font-family:"Roboto",Arial,sans-serif;font-weight:700;font-size:30px;line-height:1.25;color:var(--white)}
.hero .btn{position:absolute;left:0;top:232px;background:#1b3f13}
.hero-photo{position:absolute;right:0;top:34px;width:470px;height:260px;background:linear-gradient(135deg,#eef3e4,#cfdcbf 60%,#e8e2cf)}

/* intro */
.intro{padding-top:40px;height:720px}
.intro h2{font-size:22px}
.intro p{width:640px;margin:10px auto 0;text-align:center;font-size:12px;color:var(--muted)}
.type-cards{display:flex;gap:20px;margin-top:50px}
.type-card{position:relative;flex:1;height:410px;background:var(--panel)}
.type-card .art{position:absolute;left:40px;right:40px;top:40px;bottom:70px;background:linear-gradient(180deg,#dfe9ef,#c9d8c2)}
.type-card .label{position:absolute;bottom:-8px;background:var(--green);color:var(--white);font-family:"Roboto",Arial,sans-serif;font-weight:700;font-size:17px;padding:14px 28px;white-space:nowrap}
.type-card.computer .label{right:0}
.type-card.manual .label{left:0}

/* other products */
.products{height:420px;padding-top:10px}
.product-grid{display:flex;gap:20px;margin-top:38px}
.product{flex:1;text-align:center}
.product .thumb{height:104px;background:var(--panel);padding:10px}
.product .thumb div{height:100%}
.product h3{font-size:13px;font-weight:700;margin-top:12px}
.product p{font-size:10px;color:var(--muted);line-height:1.4;margin-top:4px;padding:0 10px}
.product .price{font-weight:700;color:var(--green-dark);font-size:14px;margin-top:4px}
.product .see{display:inline-block;border:1px solid var(--ink);font-size:10px;font-weight:700;padding:5px 12px;margin-top:8px}
.product.featured .see{background:var(--green-dark);color:var(--white);border-color:var(--green-dark)}

/* layout */
.by-layout{height:540px}
.layout-body{display:flex;margin-top:50px;gap:60px}
.layout-art{width:470px;height:380px;background:var(--panel);padding:40px}
.layout-art div{height:100%;background:linear-gradient(180deg,#e4ecef,#cfddc7)}
.layout-list{list-style:none;padding-top:34px}
.layout-list li{display:flex;align-items:center;gap:12px;font-size:14px;height:34px}
.layout-list li.active{color:var(--green-dark);font-weight:700}
.layout-list .btn{margin-top:14px}

/* software */
.by-software{height:390px}
.software-grid{display:grid;grid-template-columns:repeat(4,1fr);gap:36px 20px;margin-top:40px}
.software{height:100px;background:var(--panel);display:flex;align-items:center;justify-content:center;gap:10px;font-size:18px;font-weight:700;color:var(--green-dark);white-space:nowrap}
.software i{width:20px;height:20px;background:var(--green);display:block;flex:none}

/* about */
.about{height:530px}
.about-body{display:flex;gap:40px;margin-top:50px}
.about-text{width:460px;font-size:12px;color:var(--muted)}
.about-text p+p{margin-top:12px}
.about-text .btn{margin-top:22px}
.about-photo{width:420px;height:340px;background:linear-gradient(135deg,#cfd6dc,#8c9aa6 55%,#5b6874)}

/* testimonials */
.testimonials{height:300px;background:var(--panel);text-align:center;padding-top:50px}
.testimonials h2{color:var(--green)}
.testimonials blockquote{width:860px;margin:24px auto 0;font-size:12px;color:var(--muted)}
.testimonials cite{display:block;font-style:normal;font-size:12px;margin-top:16px}
.dots{display:flex;gap:6px;justify-content:center;margin-top:10px}
.dots b{width:8px;height:8px;border-radius:50%;background:#999}
.dots b.on{background:var(--ink)}
.arrow{position:absolute;top:170px;font-size:22px;color:var(--ink)}

/* footer */
.site-footer{height:364px;padding-top:60px;position:relative}
.footer-cols{display:flex;gap:60px}
.footer-col h4{font-size:13px;font-weight:700;color:var(--green-dark);margin-bottom:12px}
.footer-col li{list-style:none;font-size:11px;color:var(--muted);line-height:2}
.newsletter{width:300px}
.newsletter p{font-size:11px;color:var(--muted)}
.newsletter .field{border:1px solid var(--line);height:36px;margin-top:12px;font-size:11px;color:#999;padding:9px 12px}
.newsletter .btn{display:block;text-align:center;margin-top:10px;background:var(--green-deep)}
.trust{margin-left:auto;text-align:center}
.seal{width:110px;height:110px;background:var(--green);border-radius:50%;margin:0 auto}
.cards{display:flex;gap:6px;margin-top:16px}
.cards span{width:38px;height:24px;background:#d7d7d7}
.copyright{position:absolute;left:0;right:0;bottom:0;height:44px;background:var(--green-deep);color:var(--white);font-size:10px}
.copyright .wrap{padding-top:14px}
</style>
</head>
<body>

<header class="site-header">
  <div class="wrap">
    <div class="brand"><span class="brand-mark"></span>ShopLedgerForms.net</div>
    <nav class="main-nav">
      <a class="active">Business Checks</a><a>Computer Checks</a><a>Tallybook Checks</a><a>Accessories</a><a>Reorder</a><a>Help / FAQ's</a>
    </nav>
    <div class="account">
      <span><svg width="12" height="12" viewBox="0 0 12 12"><circle cx="6" cy="4" r="3" fill="#3a9a22"/><path d="M0 12a6 5 0 0 1 12 0z" fill="#3a9a22"/></svg>LOGIN</span>
      <span><svg width="12" height="12" viewBox="0 0 12 12"><rect x="1" y="1" width="10" height="10" fill="none" stroke="#3a9a22" stroke-width="2"/></svg>REGISTER</span>
      <span><svg width="12" height="12" viewBox="0 0 12 12"><path d="M2 1l3 0 1 3-2 1a7 7 0 0 0 3 3l1-2 3 1v3c-6 1-10-3-9-9z" fill="#3a9a22"/></svg>1-800-555-0142</span>
    </div>
  </div>
</header>

<section class="hero">
  <div class="wrap">
    <h1>The Cheapest Place To Order Tallybook Checks And Computer Checks For Any Software</h1>
    <span class="btn">Order Now</span>
    <div class="hero-photo" role="img" aria-label="Fanned stack of printed computer checks in assorted colours"></div>
  </div>
</section>

<section class="intro">
  <div class="wrap">
    <h2 class="section-title">Business Computer Checks Are A Simple, Effective, And Affordable Solution</h2>
    <p>For small to midsize businesses, a selection of more than 20 colour options and security features are available, and you can add an additional signature line if you need dual signatures on your computer checks, at no extra charge.</p>
    <div class="type-cards">
      <div class="type-card computer"><div class="art" role="img" aria-label="Sheet of computer checks with voucher stubs"></div><span class="label">Computer Checks</span></div>
      <div class="type-card manual"><div class="art" role="img" aria-label="Manual desk checkbook with stubs"></div><span class="label">Manual Checks</span></div>
    </div>
  </div>
</section>

<section class="products">
  <div class="wrap">
    <h2 class="section-title">Our Other Products</h2>
    <div class="product-grid">
      <div class="product featured"><div class="thumb"><div role="img" aria-label="Software checks with box" style="background:linear-gradient(135deg,#e9efd8,#b9cf8c)"></div></div><h3>Tallybook Checks</h3><p>Voucher, Standard &amp; Wallet styles, fully matched to Tallybook software.</p><div class="price">$12.99</div><span class="see">See More</span></div>
      <div class="product"><div class="thumb"><div role="img" aria-label="Personal checks with deposit slips" style="background:linear-gradient(135deg,#f3e3d6,#d98a6f)"></div></div><h3>Cashwise Checks</h3><p>Manual &amp; computer deposit slips, Cashwise compatible.</p><div class="price">$12.99</div><span class="see">See More</span></div>
      <div class="product"><div class="thumb"><div role="img" aria-label="Stack of deposit slips" style="background:linear-gradient(135deg,#e6ecf1,#aebfd1)"></div></div><h3>Deposit Slips</h3><p>Manual &amp; computer deposit slips, matched to your checks.</p><div class="price">$11.99</div><span class="see">See More</span></div>
      <div class="product"><div class="thumb"><div role="img" aria-label="Check envelopes and stamps" style="background:linear-gradient(135deg,#eeeeee,#b8b8b8)"></div></div><h3>Check Accessories</h3><p>Browse our fine selection of check envelopes &amp; self-inking stamps.</p><div class="price">$9.99</div><span class="see">See More</span></div>
    </div>
  </div>
</section>

<section class="by-layout">
  <div class="wrap">
    <h2 class="section-title">Checks By Layout</h2>
    <div class="layout-body">
      <div class="layout-art"><div role="img" aria-label="Voucher computer check layout sample"></div></div>
      <ul class="layout-list">
        <li><svg width="12" height="10" viewBox="0 0 12 10"><path d="M1 5l3 3 7-7" fill="none" stroke="#3a9a22" stroke-width="2"/></svg>Voucher Computer</li>
        <li><svg width="12" height="10" viewBox="0 0 12 10"><path d="M1 5l3 3 7-7" fill="none" stroke="#3a9a22" stroke-width="2"/></svg>Computer Middle</li>
        <li><svg width="12" height="10" viewBox="0 0 12 10"><path d="M1 5l3 3 7-7" fill="none" stroke="#3a9a22" stroke-width="2"/></svg>Computer Bottom</li>
        <li><svg width="12" height="10" viewBox="0 0 12 10"><path d="M1 5l3 3 7-7" fill="none" stroke="#3a9a22" stroke-width="2"/></svg>Computer 3 per page</li>
        <li class="active"><svg width="12" height="10" viewBox="0 0 12 10"><path d="M1 5l3 3 7-7" fill="none" stroke="#3a9a22" stroke-width="2"/></svg>Computer Wallet Personal</li>
        <li><svg width="12" height="10" viewBox="0 0 12 10"><path d="M1 5l3 3 7-7" fill="none" stroke="#3a9a22" stroke-width="2"/></svg>1 Part Desktop Manual</li>
        <li><svg width="12" height="10" viewBox="0 0 12 10"><path d="M1 5l3 3 7-7" fill="none" stroke="#3a9a22" stroke-width="2"/></svg>Duplicate Desktop Manual</li>
        <li><span class="btn">Get Started</span></li>
      </ul>
    </div>
  </div>
</section>

<section class="by-software">
  <div class="wrap">
    <h2 class="section-title">Checks By Software</h2>
    <div class="software-grid">
      <div class="software"><i></i>Tallybook</div>
      <div class="software">Cashwise</div>
      <div class="software"><i></i>Birchline</div>
      <div class="software">Mossledger</div>
      <div class="software"><i></i>Northgate Dynamics</div>
      <div class="software"><i></i>AcctBridge</div>
      <div class="software">DeedFlow</div>
      <div class="software"><i></i>PayTalent</div>
    </div>
  </div>
</section>

<section class="about">
  <div class="wrap">
    <h2 class="section-title">Who We Are</h2>
    <div class="about-body">
      <div class="about-text">
        <p>Welcome to the online ordering system of ShopLedgerForms.net, online ordering at its best. ShopLedgerForms.net provides the most comprehensive business check experience and selection available online, including traditional manual desktop checks, checks with Tallybook and other accounting software, and an extensive selection of computer checks.</p>
        <p>Our computer checks are available in many layout styles and colours, and range from layouts compatible with Tallybook software, linked directly to checks compatible with all software developed by Mossledger, Birchline, Northgate Dynamics, AcctBridge, DeedFlow, PayTalent and many other accounting programs.</p>
        <span class="btn">Read More</span>
      </div>
      <div class="about-photo" role="img" aria-label="Team of colleagues working together at a laptop in a bright office"></div>
    </div>
  </div>
</section>

<section class="testimonials">
  <div class="wrap">
    <h2 class="section-title">Client Testimonials</h2>
    <span class="arrow" style="left:-20px">‹</span><span class="arrow" style="right:-20px">›</span>
    <blockquote>Just want to thank you for the most recent checks and deposit slip order from you. It's perfect now. Great quality paper and the customer service was exceptional, and at a very reasonable price plus free shipping too. I'll refer you to all my friends. This is the first check order we've ever placed online and found the ordering and shipping experience to be exceptional. Thanks! Happy Customer!</blockquote>
    <cite>Dana R, Reno, NV. Apr 5</cite>
    <div class="dots"><b class="on"></b><b></b><b></b></div>
  </div>
</section>

<footer class="site-footer">
  <div class="wrap">
    <div class="footer-cols">
      <div class="footer-col"><h4>Information</h4><ul><li>About Us</li><li>Privacy &amp; Security</li><li>Refunds &amp; Returns</li><li>Terms &amp; Conditions</li><li>Fast Order</li></ul></div>
      <div class="footer-col"><h4>Support</h4><ul><li>Contact Us</li><li>Shipping &amp; Turnaround</li><li>Help FAQ's</li><li>Order Status</li><li>Reorder</li></ul></div>
      <div class="footer-col newsletter"><h4>Subscribe To Our Newsletter</h4><p>Get our latest deals and exclusive offers.</p><div class="field">Enter Your Email</div><span class="btn">Subscribe</span></div>
      <div class="trust"><div class="seal"></div><div class="cards"><span></span><span></span><span></span><span></span><span></span></div></div>
    </div>
  </div>
  <div class="copyright"><div class="wrap">Copyright © 2019 ShopLedgerForms.net. All Rights Reserved.</div></div>
</footer>

</body>
</html>
```